New Business card design to reflect rebrand

I would like a business card design with a good base colour for our new logo and also a placeholder for a profile pic of the card holder. the design needs to be editable to the point that we can easily change the picture of the person and use that design for printmoor etc. we are looking at a metalic finish business card so will need a good base colour to bring out the finish.

Target Market(s)

prospective customers

Industry/Entity Type

Business

Contact Information for Business Card

I would like one editable design that we can change the name of the card holder and profile picture. The design need to be in a format that be send to printmoor etc.

Our address is Fenwick Lodge, Mill Lane, Ashcombe Green, RG41 3TQ Tel no. 01632 960417

Requirements
Must have
• place holder for a profile pic for the card holder. in AI or preferably PSD format

```html
<!DOCTYPE html>
<html lang="en">
<head>
<meta charset="utf-8">
<title>Northvale Workplace Services – Business Cards</title>
<link rel="stylesheet" href="https://fonts.googleapis.com/css2?family=Open+Sans:wght@400;600;700&family=Oswald:wght@500;600&display=swap">
<style>
  :root {
    --stage: #1b1b1c;
    --card-dark: #2b2b2d;
    --card-dark-edge: #232325;
    --card-light: #f4f4f2;
    --brand-blue: #5f7a9c;
    --brand-orange: #e8702e;
    --ink: #3a4a63;
    --muted: #8a8f98;
  }
  * { box-sizing: border-box; margin: 0; padding: 0; }
  html, body { width: 1200px; height: 900px; overflow: hidden; }
  body {
    background: var(--stage);
    font-family: "Open Sans", sans-serif;
    position: relative;
  }
  .card {
    position: absolute;
    width: 525px;
    height: 300px;
    overflow: hidden;
    box-shadow: 0 10px 30px rgba(0,0,0,.5);
  }
  .card--front { left: 50px; top: 90px; background: radial-gradient(ellipse at 60% 40%, #333336, var(--card-dark-edge)); }
  .card--back { left: 625px; top: 90px; background: var(--card-light); }
  .card--portrait { left: 337px; top: 500px; background: radial-gradient(ellipse at 60% 40%, #333336, var(--card-dark-edge)); }

  .band { position: absolute; }
  .band svg { display: block; }

  /* front */
  .front-logo {
    position: absolute; left: 0; right: 0; top: 92px;
    text-align: center; color: var(--brand-blue);
    font-weight: 700; line-height: 1;
  }
  .front-logo .logo-mark {
    display: inline-block; width: 16px; height: 16px;
    background: var(--brand-orange); margin-right: 10px; vertical-align: 4px;
  }
  .front-logo .logo-name { font-size: 40px; letter-spacing: 2px; }
  .front-logo .logo-sub { display: block; font-size: 15px; letter-spacing: 5px; margin-top: 8px; }
  .front-web {
    position: absolute; left: 0; right: 0; top: 178px;
    text-align: center; color: var(--brand-orange); font-size: 14px; letter-spacing: .5px;
  }
  .services {
    position: absolute; left: 0; right: 0; top: 218px;
    display: flex; justify-content: center; gap: 10px;
    list-style: none; color: var(--brand-blue); font-size: 12.5px;
  }
  .services li::before {
    content: ""; display: inline-block; width: 6px; height: 6px;
    background: var(--brand-orange); margin-right: 6px; vertical-align: 2px;
  }

  /* back */
  .holder { position: absolute; left: 36px; top: 62px; }
  .holder-name {
    font-family: "Oswald", sans-serif; font-weight: 600;
    font-size: 36px; letter-spacing: .5px; color: var(--ink); line-height: 1;
  }
  .holder-name .surname { color: var(--brand-orange); }
  .holder-role {
    font-family: "Oswald", sans-serif; font-weight: 500;
    font-size: 15px; letter-spacing: 1.5px; color: var(--ink); margin-top: 4px;
  }
  .contact { position: absolute; left: 36px; top: 140px; list-style: none; color: var(--ink); font-size: 13px; font-weight: 600; }
  .contact li { display: flex; align-items: flex-start; margin-bottom: 6px; line-height: 1.35; }
  .contact .icon {
    flex: none; width: 18px; height: 18px; border-radius: 50%;
    background: var(--brand-orange); margin-right: 10px; margin-top: 1px;
    display: flex; align-items: center; justify-content: center;
  }
  .contact .icon svg { width: 10px; height: 10px; }

  /* portrait */
  .profile-photo {
    position: absolute; left: 320px; top: 30px; width: 140px; height: 140px;
    border: 3px solid var(--brand-blue);
    background: linear-gradient(160deg, #6b6a68, #3c3b3a 60%, #2a2a2b);
  }
  .portrait-logo {
    position: absolute; right: 40px; top: 190px; text-align: right;
    color: var(--brand-blue); font-weight: 700; line-height: 1;
  }
  .portrait-logo .logo-mark { display: inline-block; width: 12px; height: 12px; background: var(--brand-orange); margin-right: 8px; vertical-align: 3px; }
  .portrait-logo .logo-name { font-size: 30px; letter-spacing: 1.5px; }
  .portrait-logo .logo-sub { display: block; font-size: 11px; letter-spacing: 4px; margin-top: 6px; }
</style>
</head>
<body>

  <!-- Front -->
  <section class="card card--front">
    <div class="band" style="left:230px;top:0">
      <svg width="295" height="26"><polygon points="0,0 295,0 295,26 20,26" fill="var(--brand-blue)"/></svg>
    </div>
    <div class="band" style="left:0;top:66px">
      <svg width="170" height="18"><polygon points="0,0 170,0 152,18 0,18" fill="var(--brand-orange)"/></svg>
    </div>
    <div class="band" style="left:200px;top:282px">
      <svg width="325" height="18"><polygon points="18,0 325,0 325,18 0,18" fill="var(--brand-orange)"/></svg>
    </div>
    <div class="front-logo">
      <span class="logo-mark"></span><span class="logo-name">NORTHVALE</span>
      <span class="logo-sub">WORKPLACE SERVICES</span>
    </div>
    <div class="front-web">www.northvale-ws.com</div>
    <ul class="services">
      <li>IT Solutions</li><li>Networks</li><li>Telecoms</li><li>Internet</li><li>Electrical Services</li>
    </ul>
  </section>

  <!-- Back -->
  <section class="card card--back">
    <div class="band" style="left:270px;top:0">
      <svg width="255" height="24"><polygon points="0,0 255,0 255,24 22,24" fill="var(--brand-orange)"/></svg>
    </div>
    <div class="band" style="left:0;top:294px">
      <svg width="525" height="6"><rect width="525" height="6" fill="var(--brand-orange)"/></svg>
    </div>
    <div class="holder">
      <h1 class="holder-name">DANIEL <span class="surname">HARTWELL</span></h1>
      <p class="holder-role">GENERAL MANAGER</p>
    </div>
    <ul class="contact">
      <li><span class="icon"><svg viewBox="0 0 10 10"><path d="M2 1l2 2-1 1c.6 1.2 1.8 2.4 3 3l1-1 2 2-1.5 1.5C4.5 9 1 5.5.5 2.5z" fill="#fff"/></svg></span>01632 960417</li>
      <li><span class="icon"><svg viewBox="0 0 10 10"><rect x="1" y="2.5" width="8" height="5" fill="#fff"/><path d="M1 2.5l4 3 4-3" stroke="var(--brand-orange)" fill="none"/></svg></span>info@northvale-ws.com</li>
      <li><span class="icon"><svg viewBox="0 0 10 10"><circle cx="5" cy="5" r="3.8" stroke="#fff" fill="none"/><path d="M1.2 5h7.6M5 1.2c-2 2.5-2 5.1 0 7.6M5 1.2c2 2.5 2 5.1 0 7.6" stroke="#fff" fill="none" stroke-width=".8"/></svg></span>www.northvale-ws.com</li>
      <li><span class="icon"><svg viewBox="0 0 10 10"><path d="M5 9.5C3 7 2 5.5 2 4a3 3 0 016 0c0 1.5-1 3-3 5.5z" fill="#fff"/><circle cx="5" cy="4" r="1" fill="var(--brand-orange)"/></svg></span>Fenwick Lodge, Mill Lane,<br>Ashcombe Green, RG41 3TQ</li>
    </ul>
  </section>

  <!-- Front with profile picture -->
  <section class="card card--portrait">
    <div class="band" style="left:0;top:274px">
      <svg width="180" height="26"><polygon points="0,0 160,0 180,26 0,26" fill="var(--brand-blue)"/></svg>
    </div>
    <div class="profile-photo" role="img" aria-label="Profile photo of the card holder"></div>
    <div class="portrait-logo">
      <span class="logo-mark"></span><span class="logo-name">NORTHVALE</span>
      <span class="logo-sub">WORKPLACE SERVICES</span>
    </div>
  </section>

</body>
</html>
```